Nine Rung Ledger Remedy Seminar

I would like a flyer to hand out to participants at the speeches that we give. We are a CPA firm that specializes in entrepreneurs and realtors. We would like a flyer that looks crisp and clean, that integrates our logo and our company colors (shades of blue & gold). We would like the wording to be as laid out in the attached documents, but design is up to you. We would like a picture to go along with each point and are open to ideas. The flyer should be one page, preferably just the front.

Colors
3176b5
fee18a

Requirements
Must have
• Our logo and the wording supplied.
• A picture to go along with each topic.
Nice to have
• Images that pop, clean look, professional.
Should not have
• Look messy.

```html
<!DOCTYPE html>
<html lang="en">
<head>
<meta charset="utf-8">
<title>Nine Rung Ledger Remedy Seminar Agenda</title>
<link href="https://fonts.googleapis.com/css2?family=Fira+Sans+Extra+Condensed:wght@600&family=Fira+Sans+Condensed:wght@300&family=Source+Sans+3:ital,wght@0,400;0,700;1,400&family=Libre+Baskerville:ital,wght@1,700&display=swap" rel="stylesheet">
<style>
  :root {
    --panel-blue: #4c6bb0;
    --panel-deep: #3d5ca4;
    --photo-sky: #6b82b8;
    --photo-sea: #5a74b0;
    --photo-warm: #7d7fa8;
    --number-blue: #27488f;
    --brand-blue: #3176b5;
    --gold: #c9a23d;
    --gold-light: #f3df97;
    --ink: #5a5a5a;
    --ink-dark: #333;
    --paper: #ffffff;
  }
  * { box-sizing: border-box; margin: 0; padding: 0; }
  html, body { width: 895px; height: 1200px; overflow: hidden; background: var(--paper); }
  .flyer { position: relative; width: 895px; height: 1200px; font-family: "Source Sans 3", sans-serif; }

  .side-panel {
    position: absolute; left: 0; top: 0; width: 414px; height: 1200px;
    background: var(--panel-blue);
  }
  .side-photo {
    position: absolute; left: 0; top: 560px; width: 414px; height: 640px;
    background:
      radial-gradient(ellipse 150px 230px at 250px 330px, var(--photo-warm) 0%, rgba(125,127,168,0) 100%),
      linear-gradient(180deg, var(--panel-blue) 0%, var(--photo-sky) 35%, var(--photo-sea) 62%, var(--panel-deep) 100%);
  }
  .title {
    position: absolute; left: 32px; top: 150px; width: 370px;
    font-family: "Fira Sans Extra Condensed", sans-serif; font-weight: 600;
    font-size: 70px; line-height: 80px; color: #fff; letter-spacing: -0.5px;
  }
  .slogan {
    position: absolute; left: 39px; top: 787px;
    font-style: italic; font-size: 34px; line-height: 43px; color: #fff;
  }

  .brand { position: absolute; right: 31px; top: 34px; text-align: right; }
  .brand-name {
    font-weight: 700; font-size: 52px; line-height: 62px;
    color: var(--brand-blue); letter-spacing: -0.5px;
  }
  .brand-tagline {
    margin-top: 40px;
    font-family: "Libre Baskerville", serif; font-style: italic; font-weight: 700;
    font-size: 14px; color: var(--ink-dark);
  }

  .agenda {
    position: absolute; left: 433px; top: 196px; width: 434px;
    list-style: none; display: flex; flex-direction: column; gap: 20px;
  }
  .agenda-item { display: flex; gap: 12px; }
  .step-number {
    flex: 0 0 40px; height: 40px; border-radius: 4px;
    background: var(--number-blue); color: #fff;
    font-weight: 700; font-size: 23px; line-height: 40px; text-align: center;
  }
  .step-text {
    font-size: 17px; line-height: 20px; color: var(--ink);
    text-align: justify; hyphens: auto;
  }

  .motto-band {
    position: absolute; left: 0; top: 976px; width: 895px; height: 71px;
    background: linear-gradient(90deg, var(--gold) 0%, #ddbf62 30%, var(--gold-light) 50%, #ddbf62 72%, var(--gold) 100%);
    color: #fff; font-size: 28px; line-height: 71px; padding-left: 34px;
  }

  .footer-intro {
    position: absolute; left: 0; top: 1047px; width: 414px; height: 153px;
    color: #fff; font-size: 13px; line-height: 17.5px; padding: 42px 50px 0 39px;
  }
  .contact {
    position: absolute; left: 414px; top: 1047px; width: 481px; height: 153px;
    text-align: center; padding-top: 30px; font-style: normal;
    font-family: "Fira Sans Condensed", sans-serif; font-weight: 300;
    font-size: 14px; line-height: 20.5px; color: var(--ink-dark);
  }
  .contact-pair span + span { margin-left: 28px; }
</style>
</head>
<body>
<div class="flyer">
  <div class="side-panel">
    <div class="side-photo" role="img" aria-label="Faded blue-toned photo of a person relaxing in a beach chair by the sea"></div>
    <h1 class="title">Nine Rung Ledger Remedy Seminar Agenda</h1>
    <p class="slogan">Less Tax.<br>More Fun.<br>Tallied Outcomes.</p>
  </div>

  <header class="brand">
    <div class="brand-name">Tallied Outcomes</div>
    <div class="brand-tagline">A Professional Accounting Corporation</div>
  </header>

  <ol class="agenda">
    <li class="agenda-item"><span class="step-number">1.</span><p class="step-text">We will first show you how to eliminate much of your self-employment tax on your return by converting your business into an S Corporation. A business owner making over $120,000 per year can save about $12,000 per year by doing this.</p></li>
    <li class="agenda-item"><span class="step-number">2.</span><p class="step-text">We will show you how to get tax free income from your corporation by renting you home to the corporation for the board meetings. Many of our clients are getting up to $21,000 in tax free income which could put $8,400 cash into your pocket.</p></li>
    <li class="agenda-item"><span class="step-number">3.</span><p class="step-text">We will show you the easiest way to track your expenses so that the only thing you will have to do to have rock solid books is to take a picture of the receipt and throw it away. It doesn’t get any better than that.</p></li>
    <li class="agenda-item"><span class="step-number">4.</span><p class="step-text">Next, we show you the importance of tax planning and why it is critical to meet with your CPA before the end of the year and not just when you do your tax preparation.</p></li>
    <li class="agenda-item"><span class="step-number">5.</span><p class="step-text">We will show you how to hire your children and get $7,500 per child tax free. This will save you $3,000 per child in income tax reduction.</p></li>
    <li class="agenda-item"><span class="step-number">6.</span><p class="step-text">We will discuss how to make your child’s college education tax deductible. With college cost spiraling out of control this is a biggie. Most of our clients have a savings of about $12,000 per year of college.</p></li>
    <li class="agenda-item"><span class="step-number">7.</span><p class="step-text">Our grand finale is to show you how to use, not one, but two corporations to get a several hundred thousand dollar tax deferral, get an interest free loan from the government and use that money to grow your business and your wealth.</p></li>
  </ol>

  <div class="motto-band">If they drive by with a machine gun you don’t have to stand up.</div>

  <p class="footer-intro">We are a full-service Accounting firm licensed in CA. We offer a broad range of services for business owners, executives, and independent professionals. We are affordable, experienced, and friendly.</p>

  <address class="contact">
    <div>Tallied Outcomes, A Professional Accounting Corporation</div>
    <div>2870 N. Orchard Ave, Ste. B, Larkvale, CA 95012</div>
    <div class="contact-pair"><span>Phone: 555-014-2237</span><span>Fax: 555-014-2290</span></div>
    <div class="contact-pair"><span>Dalton@talliedoutcomescpas.com</span><span>Marcus@talliedoutcomescpas.com</span></div>
    <div>www.talliedoutcomescpa.com</div>
  </address>
</div>
</body>
</html>
```